Plover Scrap Ireland

Hi There,

We are a biofuels company based in Ireland. We produce biodiesel from waste cooking oils from restaurants and biogas from food waste.

We are mainly a B2B company - essentially we take from collectors of these products and they aggregate for us.

We would like to start collections of our own for both waste cooking oil
and food waste from restaurants, hotels, hospitals and offices. We will pay for the waste oil (a main focus) and charge competitive rates for the food waste - all will go to renewable solutions.

Can you design a logo for this business? And then also can you provide a leaflet outline so we can send to businesses/ post on social media. Emphasis should be on the circular model of our business.
Updates

Target Market(s)

Restaurants and Businesses

Industry/Entity Type

Waste Collection

Colors
0094D4
00A9DD
6FCCEA
C7EBF8
E9F6FB
00AB8E
00BBA5
67D7C9
C6EFE9
E9F9F6
59FF00
82FF00
B8FF75
E3FFCB
F4FFEA
FFF300
FFF600
FEFA6F
FFFEC7
FFFEE8

Requirements
Nice to have
• Renewable Ideas, Circular Nature

```html
<!DOCTYPE html>
<html lang="en">
<head>
<meta charset="UTF-8">
<title>UCO &amp; Food Waste Collection – Plover Scrap Ireland</title>
<link href="https://fonts.googleapis.com/css2?family=Montserrat:wght@400;500;600;700;800;900&display=swap" rel="stylesheet">
<style>
  :root {
    --teal: #00bba5;
    --teal-deep: #00ab8e;
    --lime: #b8ff75;
    --white: #ffffff;
    --ink: #111111;
    --photo-sky: #8fb3d6;
    --photo-field: #3c5a22;
    --nozzle-bg: #f4f4f4;
  }
  * { box-sizing: border-box; margin: 0; padding: 0; }
  html, body { width: 753px; height: 1200px; overflow: hidden; background: #fff; }
  body { font-family: "Montserrat", sans-serif; }

  .leaflet { position: relative; width: 753px; height: 1200px; display: flex; }

  .panel-uco {
    position: relative; width: 395px; height: 100%;
    background: var(--teal); color: var(--white);
  }
  .panel-uco > * { position: absolute; left: 32px; }

  .main-title { top: 40px; font-size: 36px; line-height: 44px; font-weight: 900; letter-spacing: 0.3px; }
  .main-title .by { font-weight: 500; display: block; }

  .tagline { top: 292px; font-size: 30px; line-height: 35px; font-weight: 900; }

  .intro { top: 424px; width: 300px; font-size: 14px; line-height: 22px; font-weight: 600; }

  .uco-heading { top: 572px; font-size: 30px; line-height: 38px; font-weight: 500; }
  .uco-sub { top: 684px; font-size: 20px; font-weight: 500; }

  .check-list { list-style: none; }
  .check-list li { position: relative; padding-left: 24px; }
  .check-list svg { position: absolute; left: 0; top: 3px; width: 12px; height: 12px; }

  .uco-list { top: 736px; width: 330px; font-size: 13px; line-height: 17.5px; font-weight: 500; }
  .uco-list li + li { margin-top: 14px; }

  .uco-close { top: 904px; width: 330px; font-size: 13.5px; line-height: 18px; font-weight: 500; }

  .cta {
    left: 0 !important; top: 1033px; width: 359px; height: 144px;
    background: var(--lime); color: var(--ink);
    border-radius: 0 12px 12px 0;
    padding: 34px 0 0 32px; font-size: 21px; line-height: 24px;
  }
  .cta strong { font-weight: 900; display: block; }

  .panel-food { position: relative; flex: 1; height: 100%; background: var(--white); color: var(--ink); }

  .photo-plant {
    position: absolute; top: 0; left: 0; width: 100%; height: 632px;
    background: linear-gradient(180deg, var(--photo-sky) 0%, #c9d6e2 35%, #9aa08a 52%, #5d7a34 68%, var(--photo-field) 100%);
  }

  .food-content { position: absolute; left: 21px; top: 645px; width: 320px; }
  .food-heading { font-size: 30px; line-height: 36px; font-weight: 500; }
  .food-sub { margin-top: 10px; font-size: 18px; line-height: 25px; font-weight: 600; }
  .food-list { margin-top: 10px; font-size: 13px; line-height: 17.5px; font-weight: 500; }
  .food-list li + li { margin-top: 14px; }
  .why-heading { margin-top: 26px; font-size: 18px; font-weight: 800; }
  .why-list { margin-top: 6px; font-size: 13px; line-height: 17.5px; font-weight: 500; }
  .why-list li + li { margin-top: 12px; }

  .photo-nozzle {
    position: absolute; left: 0; bottom: 0; width: 100%; height: 134px;
    background: linear-gradient(90deg, var(--nozzle-bg) 0%, #d9b3b3 55%, #f4f4f4 100%);
  }
</style>
</head>
<body>
<main class="leaflet">
  <section class="panel-uco">
    <h1 class="main-title">UCO &amp;<br>FOOD WASTE<br>COLLECTION<span class="by">BY PLOVER SCRAP<br>IRELAND</span></h1>

    <h2 class="tagline">Turning Waste<br>into Sustainable<br>Energy</h2>

    <p class="intro">At Plover Scrap Ireland, we transform food waste into biogas and used cooking oil (UCO) into biodiesel—produced right here in Ireland.</p>

    <h2 class="uco-heading">Used Cooking Oil<br>(UCO) Collection</h2>
    <p class="uco-sub">Get Paid for Your Waste!</p>

    <ul class="check-list uco-list">
      <li><svg viewBox="0 0 12 12"><circle cx="6" cy="6" r="6" fill="#fff"/><path d="M3.3 6.2 5.2 8 8.8 4.2" stroke="#00bba5" stroke-width="1.6" fill="none"/></svg>We offer competitive prices for your used cooking oil and guarantee collection within 48 hours.</li>
      <li><svg viewBox="0 0 12 12"><circle cx="6" cy="6" r="6" fill="#fff"/><path d="M3.3 6.2 5.2 8 8.8 4.2" stroke="#00bba5" stroke-width="1.6" fill="none"/></svg>Our service caters to the hospitality and food production sectors, including restaurants, bars, hotels, event venues, hospitals, and workplace canteens</li>
    </ul>

    <p class="uco-close">Choose Plover Scrap Ireland for fast, reliable UCO collection and enjoy the peace of mind of knowing your waste is being turned into clean, green biodiesel.</p>

    <div class="cta">Join the Movement Toward a Greener Future.<strong>Contact Plover Scrap Ireland Today!</strong></div>
  </section>

  <section class="panel-food">
    <div class="photo-plant" role="img" aria-label="Photo of a biofuel plant with silos and a chimney behind a green maize field under a blue sky"></div>

    <div class="food-content">
      <h2 class="food-heading">Food Waste<br>Collection</h2>
      <p class="food-sub">Affordable. Sustainable.<br>Hassle-Free.</p>
      <ul class="check-list food-list">
        <li><svg viewBox="0 0 12 12"><circle cx="6" cy="6" r="6" fill="#00bba5"/><path d="M3.3 6.2 5.2 8 8.8 4.2" stroke="#fff" stroke-width="1.6" fill="none"/></svg>Reduce your costs with our food waste bin service, starting at just €10 per lift for a 240L bin.</li>
        <li><svg viewBox="0 0 12 12"><circle cx="6" cy="6" r="6" fill="#00bba5"/><path d="M3.3 6.2 5.2 8 8.8 4.2" stroke="#fff" stroke-width="1.6" fill="none"/></svg>Keep your kitchen sustainable while helping Ireland achieve its net-zero targets.</li>
      </ul>
      <h3 class="why-heading">Why Choose Us?</h3>
      <ul class="check-list why-list">
        <li><svg viewBox="0 0 12 12"><circle cx="6" cy="6" r="6" fill="#00bba5"/><path d="M3.3 6.2 5.2 8 8.8 4.2" stroke="#fff" stroke-width="1.6" fill="none"/></svg>Monthly bin cleaning included!</li>
        <li><svg viewBox="0 0 12 12"><circle cx="6" cy="6" r="6" fill="#00bba5"/><path d="M3.3 6.2 5.2 8 8.8 4.2" stroke="#fff" stroke-width="1.6" fill="none"/></svg>All food waste is converted into biomethane at our anaerobic digestion facility in Meath.</li>
      </ul>
    </div>

    <div class="photo-nozzle" role="img" aria-label="Illustration of a red fuel pump nozzle with a drop of oil and a black hose"></div>
  </section>
</main>
</body>
</html>
```